Crestline Lending Group Business Cards

We are looking to revamp the current business cards each of our locations uses. We are a lending company that specializes in personal loans, title loans, and tax services. We have locations in New Mexico, Texas, and Oklahoma.

We would like a cleaner, sleeker look while still highlighting what we offer. Title Loans, Personal Loans & Tax Services. We also want to include our referral fee somewhere on the card. We would like to see an English option as well as a Spanish option for the cards.

PLEASE NOTE: Some business cards do not include the employee's name but just the store's location, while others will include both.

These are double-sided business cards, and we would like to see proof if possible. I have included proofs of our current business cards for you to review below, as well as our company logo. Feel free to get creative with the logo, etc! Colors should match the logo; however, you do not need to use all of our logo colors if you don't want to.

```html
<!DOCTYPE html>
<html lang="en">
<head>
<meta charset="utf-8">
<title>Crestline Lending Group – Business Cards</title>
<link rel="stylesheet" href="https://fonts.googleapis.com/css2?family=Montserrat:wght@600;700;800&family=Poppins:ital,wght@0,800;1,800&display=swap">
<style>
  :root {
    --backdrop: #58595b;
    --brand-red: #c1232a;
    --brand-green: #124f2f;
    --paper: #ffffff;
    --ink-gray: #555657;
  }
  * { margin: 0; padding: 0; box-sizing: border-box; }
  html, body { width: 1200px; height: 1200px; overflow: hidden; }
  body { background: var(--backdrop); position: relative; font-family: "Montserrat", sans-serif; }

  .card {
    position: absolute;
    left: 197px;
    width: 806px;
    height: 460px;
    background: var(--paper);
    overflow: hidden;
    box-shadow: 0 10px 18px rgba(0,0,0,0.35);
  }
  .card--front { top: 120px; }
  .card--back { top: 619px; }
  .card__art { position: absolute; inset: 0; width: 100%; height: 100%; }

  /* Brand wordmark */
  .brand-name {
    position: absolute;
    font-family: "Montserrat", sans-serif;
    font-weight: 800;
    line-height: 1.05;
    white-space: nowrap;
  }
  .brand-name--front { left: 30px; top: 140px; font-size: 34px; color: var(--brand-green); }
  .brand-name--back { left: 30px; top: 345px; font-size: 26px; color: var(--paper); }

  /* Front */
  .staff { position: absolute; left: 469px; top: 118px; }
  .staff__name { font-weight: 800; font-size: 38px; color: var(--brand-green); letter-spacing: 0.5px; line-height: 1; }
  .staff__role { font-weight: 700; font-size: 20px; color: var(--brand-red); letter-spacing: 1.2px; margin-top: 6px; }

  .contact { position: absolute; left: 432px; top: 218px; list-style: none; }
  .contact__item {
    display: flex; align-items: flex-start; gap: 14px;
    font-weight: 700; font-size: 20px; color: var(--ink-gray);
    letter-spacing: 1.6px; line-height: 27px; margin-bottom: 7px;
    white-space: nowrap;
  }
  .contact__icon { width: 22px; height: 22px; flex: none; margin-top: 3px; fill: var(--brand-red); }

  .services {
    position: absolute; left: 28px; top: 336px; list-style: none;
    font-family: "Poppins", sans-serif; font-style: italic; font-weight: 800;
    font-size: 26px; letter-spacing: 2.4px; color: var(--paper); line-height: 35.5px;
  }
  .services li::before { content: "•"; margin-right: 6px; }

  /* Back */
  .referral {
    position: absolute;
    font-family: "Poppins", sans-serif; font-style: italic; font-weight: 800;
    line-height: 1; white-space: nowrap;
  }
  .referral__lead { left: 82px; top: 132px; font-size: 38px; color: var(--brand-green); letter-spacing: 1px; }
  .referral__offer { left: 74px; top: 178px; font-size: 56px; color: var(--brand-red); letter-spacing: 2px; }
  .referral__amount { left: 390px; top: 104px; font-size: 136px; color: var(--brand-red); letter-spacing: 4px; }
</style>
</head>
<body>

<section class="card card--front" aria-label="Card front">
  <svg class="card__art" viewBox="0 0 1298 741" preserveAspectRatio="none" aria-hidden="true">
    <path d="M733 0 L1298 0 L1298 157 C1150 162 950 95 733 0 Z" fill="var(--brand-red)"/>
    <path d="M573 0 L700 0 C800 40 880 90 948 135 C850 92 720 30 573 0 Z" fill="var(--brand-green)"/>
    <path d="M0 412 C200 395 400 480 600 575 C800 655 1050 680 1298 652 L1298 741 L0 741 Z" fill="var(--brand-red)"/>
    <path d="M761 590 C900 640 1100 632 1298 582 L1298 622 C1100 652 900 642 761 590 Z" fill="var(--brand-green)"/>
    <rect x="646" y="192" width="4" height="360" fill="var(--brand-green)"/>
  </svg>

  <p class="brand-name brand-name--front">Crestline<br>Lending Group</p>

  <div class="staff">
    <h1 class="staff__name">JONE DOE</h1>
    <p class="staff__role">Branch Manager</p>
  </div>

  <ul class="contact">
    <li class="contact__item">
      <svg class="contact__icon" viewBox="0 0 24 24" aria-hidden="true"><path d="M6.6 10.8a15.1 15.1 0 0 0 6.6 6.6l2.2-2.2c.3-.3.7-.4 1-.2 1.1.4 2.3.6 3.6.6.6 0 1 .4 1 1V20c0 .6-.4 1-1 1A17 17 0 0 1 3 4c0-.6.4-1 1-1h3.5c.6 0 1 .4 1 1 0 1.3.2 2.5.6 3.6.1.3 0 .7-.2 1z"/></svg>
      <span>(505) 555-1212</span>
    </li>
    <li class="contact__item">
      <svg class="contact__icon" viewBox="0 0 24 24" aria-hidden="true"><path d="M3 6h18v12H3z M3 6l9 7 9-7" fill="var(--brand-red)" stroke="#fff" stroke-width="1.4"/></svg>
      <span>abcde@crestline.com</span>
    </li>
    <li class="contact__item">
      <svg class="contact__icon" viewBox="0 0 24 24" aria-hidden="true"><path d="M12 2a7 7 0 0 0-7 7c0 5 7 13 7 13s7-8 7-13a7 7 0 0 0-7-7zm0 9.5A2.5 2.5 0 1 1 12 6.5a2.5 2.5 0 0 1 0 5z"/></svg>
      <span>123 Elm Street, Suite B,<br>Anytown, Texas 55555</span>
    </li>
  </ul>

  <ul class="services">
    <li>TITLE LOANS</li>
    <li>PERSONAL LOANS</li>
    <li>TAX SERVICES</li>
  </ul>
</section>

<section class="card card--back" aria-label="Card back">
  <svg class="card__art" viewBox="0 0 1298 741" preserveAspectRatio="none" aria-hidden="true">
    <path d="M733 0 L1298 0 L1298 157 C1150 162 950 95 733 0 Z" fill="var(--brand-green)"/>
    <path d="M573 0 L700 0 C800 40 880 90 948 135 C850 92 720 30 573 0 Z" fill="var(--brand-red)"/>
    <path d="M0 412 C200 395 400 480 600 575 C800 655 1050 680 1298 652 L1298 741 L0 741 Z" fill="var(--brand-green)"/>
    <path d="M761 590 C900 640 1100 632 1298 582 L1298 622 C1100 652 900 642 761 590 Z" fill="var(--brand-red)"/>
    <rect x="735" y="398" width="563" height="4" fill="var(--brand-green)"/>
  </svg>

  <p class="referral referral__lead">Refer a Friend</p>
  <p class="referral referral__offer">GET up tp</p>
  <p class="referral referral__amount">$100</p>

  <p class="brand-name brand-name--back">Crestline<br>Lending Group</p>
</section>

</body>
</html>
```